TMVG Website

Hi we require a website with similar attributes and design to this http://layout7.fernquaysites.com but obviously with all our information and images etc... also attached are our logos please do the design with the yellow logo not the red.

```html
<!DOCTYPE html>
<html lang="en">
<head>
<meta charset="utf-8">
<title>TMVG – Trimvale Collision Repair Centre</title>
<link href="https://fonts.googleapis.com/css2?family=Oswald:wght@400;500;600&family=Poppins:wght@400;500;600&family=Open+Sans:wght@400;600&display=swap" rel="stylesheet">
<style>
:root{
  --black:#000;
  --bar:#23282d;
  --gold:#e6bf0a;
  --gold-deep:#b8980f;
  --gold-line:#c9a413;
  --green:#1fa37a;
  --grey:#c8c8c8;
  --text:#dcdcdc;
  --field:#b9b9b4;
  --foot:#222;
  --panel-dark:#0e0e0e;
  --panel-mid:#1c1c1c;
}
*{margin:0;padding:0;box-sizing:border-box}
html,body{width:674px;height:1200px;overflow:hidden;background:var(--black)}
body{position:relative;font-family:"Open Sans",sans-serif;color:var(--text)}
.abs{position:absolute}
.admin-bar{left:0;top:0;width:674px;height:18px;background:var(--bar);font-size:7px;color:#eee;display:flex;align-items:center;padding:0 8px;gap:10px}
.admin-bar .right{margin-left:auto}
.brand-box{left:260px;top:42px;width:154px;height:62px;background:#3a3a3a;border:1px solid #555;display:flex;flex-direction:column;align-items:center;justify-content:center;gap:2px}
.brand-name{font-family:"Oswald",sans-serif;font-weight:600;color:var(--gold);font-size:24px;letter-spacing:3px;line-height:1}
.brand-sub{font-family:"Oswald",sans-serif;font-weight:600;color:var(--gold);font-size:9px;letter-spacing:1px}
.main-nav{left:94px;top:105px;width:484px;height:44px;background:linear-gradient(#e8c20c,#d9b208);border-bottom:2px solid #f2dc6a;display:flex;justify-content:center;align-items:center;gap:13px;font-family:"Oswald",sans-serif;font-weight:600;font-size:10px;color:#fff}
.hero{left:63px;top:228px;width:547px;height:260px;background:radial-gradient(ellipse at 55% 45%,#6a6a6a,#2a2a2a 55%,#0c0c0c)}
.hero-title{left:0;top:240px;width:674px;text-align:center;font-family:"Poppins",sans-serif;font-weight:600;font-size:40px;line-height:43px;color:var(--grey)}
.hero-btn{left:274px;top:350px;width:125px;height:37px;border:1px solid #cfcfcf;display:flex;align-items:center;justify-content:center;font-size:9.5px;color:#d8d8d8;font-family:"Poppins",sans-serif}
.gold-rule{left:67px;top:509px;width:539px;height:2px;background:var(--gold-line);box-shadow:0 3px 6px rgba(201,164,19,.5)}
.about{left:67px;top:520px;width:356px;height:364px;background:linear-gradient(180deg,var(--panel-mid),var(--panel-dark) 70%,#141414)}
.about-rule{left:67px;top:881px;width:328px;height:2px;background:var(--gold-line)}
.about-kicker{left:67px;top:534px;font-family:"Poppins",sans-serif;font-weight:400;font-size:9.5px;color:var(--green)}
.about-title{left:67px;top:547px;font-family:"Oswald",sans-serif;font-weight:400;font-size:14px;color:#ddd}
.about-copy{left:67px;top:570px;width:330px;font-size:7.2px;line-height:12px;color:#e6e6e6}
.side-head{left:425px;width:176px;height:22px;background:var(--gold);border-bottom:2px solid #fff3b0;font-family:"Oswald",sans-serif;font-weight:600;font-size:11px;color:#fff;padding:3px 5px}
.service-photo{left:425px;top:566px;width:181px;height:140px;background:linear-gradient(160deg,#6e6a4c,#4a4630 60%,#33301f)}
.service-title{left:432px;top:637px;font-family:"Oswald",sans-serif;font-size:10px;color:#ddd}
.service-copy{left:432px;top:655px;width:165px;font-family:Georgia,serif;font-size:6.2px;line-height:12px;color:#ddd}
.service-link{left:432px;top:684px;font-family:"Oswald",sans-serif;font-size:8px;color:#ddd}
.form-panel{left:425px;top:750px;width:181px;height:135px;background:var(--gold-deep)}
.field{height:17px;background:var(--field);border:1px solid #d4cfa5;font-size:7px;color:#eee;padding:3px 4px}
.submit{left:496px;top:857px;width:42px;height:21px;background:var(--gold);color:#fff;font-family:"Oswald",sans-serif;font-size:8px;display:flex;align-items:center;justify-content:center}
.promo{top:912px;width:160px;height:82px;background:linear-gradient(135deg,#c9a40c,#8a7406)}
.promo-list{list-style:none;font-size:7px;line-height:17px;color:#fff;padding:6px 8px}
.estimate-btn{left:264px;top:944px;width:120px;height:18px;background:#d9dcd6;color:#5a5a3a;font-family:"Oswald",sans-serif;font-size:8.5px;display:flex;align-items:center;justify-content:center}
.promo-text{padding:7px 8px;color:#fff;font-size:6.6px;line-height:9px}
.promo-text h3{font-family:"Oswald",sans-serif;font-weight:500;font-size:10.5px;margin-bottom:3px}
.footer-rule{left:67px;top:1031px;width:539px;height:1px;background:#888}
.social{left:72px;top:1064px;display:flex;gap:10px}
.social span{width:8px;height:8px;border-radius:50%;background:#ddd;display:block}
.foot-title{font-family:"Oswald",sans-serif;font-weight:500;font-size:11.5px;color:#ddd}
.foot-copy{font-size:6.8px;line-height:12px;color:#ddd}
.foot-brand{left:486px;top:1088px;display:flex;align-items:center;gap:5px;font-family:"Oswald",sans-serif;font-weight:600;font-size:13px;color:var(--gold)}
.foot-brand i{width:9px;height:9px;background:var(--gold);display:block}
.bottom-bar{left:0;top:1176px;width:674px;height:24px;background:var(--foot);display:flex;align-items:center;padding:0 67px;font-size:6.5px;color:#888}
.bottom-bar .dots{margin-left:auto;display:flex;gap:10px}
.bottom-bar .dots span{width:8px;height:8px;border-radius:50%;background:#777;display:block}
</style>
</head>
<body>
<div class="abs admin-bar"><span>My Sites</span><span>Car Repair</span><span>7</span><span>0</span><span>+ New</span><span>Edit Page</span><span>Enable Visual Builder</span><span class="right">Howdy, admin</span></div>

<div class="abs brand-box"><div class="brand-name">TMVG</div><div class="brand-sub">TRIMVALE COLLISION</div></div>
<nav class="abs main-nav"><span>ONLINE ESTIMATE</span><span>SERVICES</span><span>CONTACT US</span>
<svg width="9" height="9" viewBox="0 0 10 10"><circle cx="6" cy="4" r="3" fill="none" stroke="#fff" stroke-width="1.2"/><line x1="4" y1="6" x2="1" y2="9" stroke="#fff" stroke-width="1.2"/></svg></nav>

<div class="abs hero" role="img" aria-label="Black sports car in a dark studio with a glossy reflection"></div>
<h1 class="abs hero-title">HIGHLY PROFESSIONAL<br>AUTO BODY TECHINICIANS</h1>
<div class="abs hero-btn">VIEW ALL SERVICES</div>

<div class="abs gold-rule"></div>
<section class="abs about" role="img" aria-label="Dark brushed metal background"></section>
<div class="abs about-rule"></div>
<div class="abs about-kicker">WELCOME</div>
<h2 class="abs about-title">ABOUT US</h2>
<p class="abs about-copy">Lorem ipsum dolor sit amet, consectetur adipiscing elit, sed do eiusmod tempor incididunt ut labore et dolore magna aliqua. Ut enim ad minim veniam, quis nostrud exercitation ullamco laboris nisi ut aliquip ex ea commodo consequat. Duis aute irure dolor in reprehenderit in voluptate velit esse cillum dolore eu fugiat nulla pariatur. Excepteur sint occaecat cupidatat non proident, sunt in culpa qui officia deserunt mollit anim id est laborum.Excepteur sint occaecat cupidatat non proident</p>

<div class="abs side-head" style="top:536px">SERVICES</div>
<div class="abs service-photo" role="img" aria-label="Mechanic working under the bonnet of a car"></div>
<div class="abs service-title">AUTO GLASS REPAIR AND REPLACEMENT</div>
<p class="abs service-copy">Lorem ipsum dolor sit amet, consectetur adipiscing elit, sed do eiusmod tempor incididunt</p>
<div class="abs service-link">LEARN MORE</div>

<div class="abs side-head" style="top:723px">CONTACT FORM</div>
<div class="abs form-panel"></div>
<div class="abs field" style="left:433px;top:759px;width:79px">First Name</div>
<div class="abs field" style="left:518px;top:759px;width:80px">First Name</div>
<div class="abs field" style="left:433px;top:782px;width:79px">Email Address</div>
<div class="abs field" style="left:518px;top:782px;width:80px">Phone Number</div>
<div class="abs field" style="left:433px;top:805px;width:165px;height:46px">Tell Us What's On Your Mind ?</div>
<div class="abs submit">SUBMIT</div>

<div class="abs promo" style="left:67px"><ul class="promo-list"><li>Auto Body Repair</li><li>Paintless Paint Repair</li><li>Towing</li><li>Auto Body Refinishing</li></ul></div>
<div class="abs promo" style="left:257px;background:linear-gradient(135deg,#d8c23a,#a89020)" role="img" aria-label="Technician holding a spray gun, tinted gold"></div>
<div class="abs estimate-btn">GET AN ONLINE ESTIMATED</div>
<div class="abs promo" style="left:446px"><div class="promo-text"><h3>FREE DETAIL</h3>On Repair&nbsp; Over $2000<br><br>Offer Expire: 12/13/2050<br><br>Offer Void With Other Offers PRINT THIS SECTION</div></div>

<div class="abs footer-rule"></div>
<div class="abs social"><span></span><span></span><span></span></div>
<div class="abs foot-title" style="left:67px;top:1093px">TRIMVALE</div>
<div class="abs foot-copy" style="left:67px;top:1112px">412, Marlow Avenue, Riverbend Plains Texas, 75210</div>
<div class="abs foot-title" style="left:257px;top:1057px">CLIENT'S REVIEWS</div>
<p class="abs foot-copy" style="left:257px;top:1077px;width:160px">Lorem ipsum dolor sit amet, consectetur adipiscing elit, sed do eiusmod tempor incididunt ut labore et dolore magna aliqua</p>
<div class="abs foot-title" style="left:257px;top:1121px;color:var(--green);font-size:9.5px">VIEW MORE</div>
<div class="abs foot-brand"><i></i>TRIMVALE</div>

<footer class="abs bottom-bar"><span>© 2018 AUTO BODY WEBSITE DESIGN BY BRIGHTLOOP WEBSITES - ALL RIGHTS RESERVED | ADMIN LOGIN Privacy Policy</span><span class="dots"><span></span><span></span><span></span><span></span></span></footer>
</body>
</html>
```